Pellham Ridge Nectar Company, local Honey producer needs product Lable to encourage sales

We are a small business (Pellham Ridge Nectar Company) located in a small Texas town that harvests honey from our beehives yearly. Our honey would be considered "raw wildflower honey" and our goal is to sell it locally (farmers markets) and to surrounding areas.

We are currently packaging in plastic classic honey bottles with white flip caps. Sizes are 8oz and 16oz bottles (see pictures for actual size). Larger orders will be filled in one quart mason jars.

Design Ideas:
-vintage style design with bee or several bees in background
- incorporate company name "Pellham Ridge Nectar Company"
- needs small description "Raw Honey", and "Harvested in Corran Falls Valley"

Target Market(s)

Farmers markets, health conscience people looking for unprocessed food options

Industry/Entity Type

Small Business

Requirements
Nice to have
• Vintage feel
Should not have
• No cartoonish characters

```html
<!DOCTYPE html>
<html lang="en">
<head>
<meta charset="utf-8">
<title>Pellham Ridge Nectar Company – Raw Honey Label</title>
<link rel="stylesheet" href="https://fonts.googleapis.com/css2?family=Libre+Baskerville:ital,wght@0,400;0,700;1,400&display=swap">
<style>
  :root {
    --page-bg: #ffffff;
    --label-edge: #c8702c;
    --label-mid: #e6a458;
    --label-light: #f4d49a;
    --label-cream: #f7e2b4;
    --rule: #fff6e6;
    --ink: #1c140c;
    --ink-soft: #2a1f14;
    --art-dark: #7a5a2e;
    --art-light: #d9b277;
  }
  * { margin: 0; padding: 0; box-sizing: border-box; }
  html, body {
    width: 1200px;
    height: 1000px;
    overflow: hidden;
    background: var(--page-bg);
  }
  .canvas {
    position: relative;
    width: 1200px;
    height: 1000px;
  }
  .label {
    position: absolute;
    left: 320px;
    top: 85px;
    width: 560px;
    height: 830px;
    border-radius: 50% / 36%;
    background: radial-gradient(ellipse at 50% 48%, var(--label-cream) 0%, var(--label-light) 38%, var(--label-mid) 78%, var(--label-edge) 100%);
    font-family: "Libre Baskerville", Georgia, serif;
    color: var(--ink);
    text-align: center;
  }
  .label-rule {
    position: absolute;
    inset: 22px;
    border: 2px solid var(--rule);
    border-radius: 50% / 36%;
    opacity: 0.85;
  }
  .brand-top,
  .brand-bottom {
    position: absolute;
    left: 0; right: 0;
    font-style: italic;
    font-size: 34px;
    line-height: 1.2;
    color: var(--ink-soft);
  }
  .brand-top { top: 118px; }
  .brand-bottom { top: 248px; }
  .brand-main {
    position: absolute;
    left: 0; right: 0;
    top: 168px;
    font-weight: 700;
    font-size: 68px;
    letter-spacing: 2px;
    line-height: 1;
  }
  .bee-art {
    position: absolute;
    left: 110px;
    top: 330px;
    width: 340px;
    height: 270px;
    border-radius: 46%;
    background: radial-gradient(ellipse at 50% 55%, var(--art-dark) 0%, var(--art-light) 70%, transparent 100%);
    opacity: 0.75;
  }
  .product-name {
    position: absolute;
    left: 0; right: 0;
    top: 640px;
    font-weight: 700;
    font-size: 31px;
    line-height: 1.2;
  }
  .origin {
    position: absolute;
    left: 0; right: 0;
    top: 700px;
    font-style: italic;
    font-size: 21px;
    line-height: 1.2;
  }
  .net-weight {
    position: absolute;
    left: 0; right: 0;
    top: 755px;
    font-size: 21px;
    line-height: 1.2;
  }
</style>
</head>
<body>
<main class="canvas">
  <section class="label">
    <div class="label-rule"></div>
    <p class="brand-top">Pellham Ridge</p>
    <h1 class="brand-main">NECTAR</h1>
    <p class="brand-bottom">Company</p>
    <div class="bee-art" role="img" aria-label="Vintage engraved illustration of a honey bee with spread wings"></div>
    <p class="product-name">Raw Honey</p>
    <p class="origin">Harvested in Corran Falls Valley</p>
    <p class="net-weight">16oz.</p>
  </section>
</main>
</body>
</html>
```